PDF flyer to go out to Medical Providers: 2 sided A4

We need to design a 2 sided A4 pamphlet which we can email out to prospective clients.

We are a recruitment company and wish to provide staff to healthcare providers

We are a medical recruitment agency. We need to be able to write approximately 600 words, split up into 4 sub headings. Text has been provided on the uploaded word document. THIS TEXT IS DRAFT ONLY AND WILL CHANGE.

We need to look professional & efficient

Target Market(s)

Hospitals, srugeries

Industry/Entity Type

Medical

Requirements
Must have
• Room for 600 words, which will b echanged once the layout is confirmed
Nice to have
• Have it in Word form so we can use it for subsequent mail outs.

```html
<!DOCTYPE html>
<html lang="en">
<head>
<meta charset="utf-8">
<title>CareStaff Partners – Two-Sided Flyer</title>
<link rel="stylesheet" href="https://fonts.googleapis.com/css2?family=Source+Sans+3:wght@400;600&family=Tinos:wght@400&display=swap">
<style>
  :root {
    --backdrop: #c8dbe5;
    --paper: #ffffff;
    --teal: #1f7f7d;
    --teal-light: #3aa8a4;
    --teal-dark: #146868;
    --ink: #1d1d1d;
    --rule: #d3dcdc;
    --photo-a: #b9d6dc;
    --photo-b: #e8eef0;
    --photo-c: #4fb3ad;
  }
  * { box-sizing: border-box; margin: 0; padding: 0; }
  html, body { width: 1200px; height: 800px; overflow: hidden; }
  body { background: var(--backdrop); font-family: "Tinos", "Times New Roman", serif; color: var(--ink); position: relative; }

  .page {
    position: absolute; top: 46px; width: 496px; height: 702px;
    background: var(--paper); box-shadow: 0 2px 8px rgba(0,0,0,.25);
    overflow: hidden;
  }
  .page--front { left: 91px; }
  .page--back { left: 605px; }

  .page-footer { position: absolute; left: 0; right: 0; bottom: 0; height: 11px; display: flex; }
  .page-footer span { flex: 1; }
  .page-footer span:nth-child(1) { background: var(--teal-dark); }
  .page-footer span:nth-child(2) { background: var(--teal-light); }
  .page-footer span:nth-child(3) { background: var(--teal-dark); }

  .sans { font-family: "Source Sans 3", Arial, sans-serif; }

  /* Front page */
  .hero {
    position: absolute; left: 0; top: 0; width: 496px; height: 352px;
    background: linear-gradient(100deg, var(--photo-c) 0%, var(--photo-a) 30%, var(--photo-b) 65%, var(--photo-a) 100%);
  }
  .hero-band {
    position: absolute; left: 0; top: 258px; width: 496px; height: 94px;
    background: rgba(255,255,255,.72);
    display: flex; align-items: center; justify-content: center; gap: 12px;
  }
  .hero-rule { position: absolute; left: 0; top: 352px; width: 496px; height: 5px; background: var(--teal); }

  .brand { font-family: "Source Sans 3", Arial, sans-serif; font-weight: 400; color: var(--teal); line-height: 1; }
  .brand-dot { border-radius: 50%; background: var(--teal); flex: none; }
  .hero-band .brand { font-size: 36px; }
  .hero-band .brand-dot { width: 40px; height: 40px; }

  .intro-title { position: absolute; left: 33px; top: 380px; font-family: "Source Sans 3", Arial, sans-serif; color: var(--teal); }
  .intro-title h1 { font-size: 22px; font-weight: 400; line-height: 1.1; }
  .intro-title p { font-size: 15px; line-height: 1.2; }

  .body-copy { font-size: 10.4px; line-height: 15.3px; text-align: justify; }
  .small-copy { font-size: 8.2px; line-height: 13px; }

  .front-main { position: absolute; left: 33px; top: 438px; width: 226px; }
  .front-side { position: absolute; left: 276px; top: 436px; width: 190px; }
  .front-divider { position: absolute; left: 267px; top: 440px; width: 1px; height: 225px; background: var(--rule); }

  .subhead { font-family: "Source Sans 3", Arial, sans-serif; color: var(--teal); font-weight: 400; font-size: 13px; line-height: 1.2; margin-bottom: 3px; }
  .specialism-list { list-style: none; margin-top: 13px; }
  .front-side .subhead.lower { margin-top: 14px; }

  /* Back page */
  .back-head { position: absolute; left: 13px; top: 44px; display: flex; align-items: center; gap: 10px; }
  .back-head .brand-dot { width: 32px; height: 32px; opacity: .85; }
  .back-head h2 { font-family: "Source Sans 3", Arial, sans-serif; font-weight: 400; color: var(--teal); font-size: 16px; }

  .back-left { position: absolute; left: 28px; top: 88px; width: 225px; }
  .back-right { position: absolute; left: 268px; top: 89px; width: 210px; }
  .back-divider { position: absolute; left: 260px; top: 92px; width: 1px; height: 560px; background: var(--rule); }
  .back-left .subhead.mid { margin-top: 6px; margin-bottom: 12px; }
  .step { margin-bottom: 15px; }
  .step:last-child { margin-bottom: 0; }

  .feature-photo {
    position: absolute; left: 271px; top: 392px; width: 206px; height: 224px;
    background: linear-gradient(160deg, var(--photo-b) 0%, var(--photo-a) 55%, #e9eef0 100%);
  }
  .back-brand { position: absolute; left: 268px; top: 633px; display: flex; align-items: center; gap: 9px; }
  .back-brand .brand { font-size: 23px; }
  .back-brand .brand-dot { width: 30px; height: 30px; }
</style>
</head>
<body>

<section class="page page--front" aria-label="Flyer front">
  <div class="hero" role="img" aria-label="Photograph of a nurse in teal scrubs and mask pulling on gloves, with medical staff behind"></div>
  <div class="hero-band">
    <span class="brand-dot"></span>
    <span class="brand">CareStaff Partners</span>
  </div>
  <div class="hero-rule"></div>

  <div class="intro-title">
    <h1>A specialist team</h1>
    <p>dedicated to special care</p>
  </div>

  <div class="front-main body-copy">
    <p>Meridian Nursing was established with a sole focus to provide nationwide recruitment solutions for specialist sector nursing requirements. We have over 30 years industry experience and successfully deliver nursing solutions to client requirements.</p>
    <p>Our philosophy is to be masters in our supply of specialist staff rather than diluting our service by over generalising. This ethos was naturally birthed from supplying to all types of healthcare establishments and identifying a trend whereby agencies could fill easier bookings - still leaving the client with those important and hard to fill requirements and ultimately falling short of providing a full service.</p>
  </div>

  <div class="front-divider"></div>

  <div class="front-side small-copy">
    <h3 class="subhead">Our specialisms:</h3>
    <p>Our consultants provide a professional and effective service in the supply of the following speciality nurses:</p>
    <ul class="specialism-list">
      <li>Theatre (Scrub, Anaesthetics, Recovery) and ODP's</li>
      <li>A&amp;E Nurses</li>
      <li>ITU / HDU / CCU Nurses</li>
      <li>Paediatric Nurses (General Paeds, PICU &amp; NICU)</li>
      <li>RMN &amp; CPN's</li>
      <li>Oncology Nurses</li>
      <li>Community / District Nurses</li>
      <li>Midwives</li>
    </ul>
    <h3 class="subhead lower">24 Hour service:</h3>
    <p>Our consultants are available 24hrs round the clock to manage requests: Last minute adhoc, long/short term bookings, block bookings and pre-approved rotas.</p>
  </div>

  <div class="page-footer"><span></span><span></span><span></span></div>
</section>

<section class="page page--back" aria-label="Flyer back">
  <div class="back-head">
    <span class="brand-dot"></span>
    <h2>Why CareStaff Partners?</h2>
  </div>

  <div class="back-left body-copy">
    <h3 class="subhead">Selective Recruitment Drives</h3>
    <p>We recruit for a smaller skill-set than most agencies. This allows serious focus to ensure the best quality nurses are selected to represent our values and provide care for your patients.</p>
    <p>We have heavily invested in tailoring Meridian Nursing to the important requirements that remain unfilled nationwide. This strategy works hand in hand to alleviate the pressure from staff banks and procurement teams who struggle with supply of a specific speciality requirement to be filled. Meridian Nursing should be the name that is instantly thought of for provision of speciality nurses.</p>
    <h3 class="subhead mid">Our selective recruitment drive means we:</h3>
    <p class="step">1. Identify locations where consistent speciality shifts are required.</p>
    <p class="step">2. Learn from patterns i.e. busiest periods, hard to fill shifts, average amount of speciality staff utilised per week - this understanding allows our recruitment drive to be structured around your needs as a client and enables us to match staff more effectively to your requirements.</p>
    <p class="step">3. Understand the Healthcare Market:<br>Meridian Nursing is proud that our specialist consultants are the most knowledgeable in their fields. This alone sets our high standards because we know what differentiates a nurse from an excellent nurse. Our excellent nurses service our clients and are more often requested to commit to the hospitals for a longer period of time. Our expert consultants can be trusted to obtain training, inoculations and compliance which is relevant to the speciality they supply to e.g. EPP clearance's / IV's, venepuncture etc.</p>
  </div>

  <div class="back-divider"></div>

  <div class="back-right body-copy">
    <h3 class="subhead">Candidate Screening</h3>
    <p>All candidates are required to provide original identification: passport and driving licence, appropriate working visa, verified qualifications and training certificates, proof of address and relevant inoculations.</p>
    <p>We ensure every candidate has: a completed registration form and full career history, verified references covering a minimum of five years, a DBS and has fulfilled occupational health checks for fitness-to-work.</p>
    <p>Our aim is to be recognised as the industry's benchmark for excellence in nursing personnel supply to the NHS, private hospitals, nursing homes and residential care.</p>
    <p>Our tailor-made programmes and services are designed around our clients' needs to guarantee they will be delighted with the quality of our service.</p>
  </div>

  <div class="feature-photo" role="img" aria-label="Photograph of a doctor and a smiling nurse reviewing a clipboard by a window"></div>

  <div class="back-brand">
    <span class="brand-dot"></span>
    <span class="brand">CareStaff Partners</span>
  </div>

  <div class="page-footer"><span></span><span></span><span></span></div>
</section>

</body>
</html>
```